Wet Market Business Needs a Signboard Design!

We need a signboard design for a wet market management company based in Singapore. Our company name is Bo Kiat Management Pte Ltd. We manage various wet markets where people buy and sell vegetables, fish, poultry, pork and others. We would like to see designs that are able to project an image of freshness, yet being modern at the same time. However, as our main consumers are aged between 30 to 60 years old, the designs should not be overly-trendy that it fails to connect with our consumers.
Updates

Reason: Hi all, I would like to see more designs as I have not seen one that captures my heart. However, I prefer the signboard designs to be like #2680195 by Ruvo07, #2680150 by Ruvo07, #2667605 by Pelquinar, and #2653966 by Harsha Ramaprasad. Thanks!

Target Market(s)

30 years old to 60 years old.

Industry/Entity Type

Business

Requirements
Must have
• Our company logo, our company name "BO KIAT MANAGEMENT", and the words "TAMPOLI FRESH MARKET".

```html
<!DOCTYPE html>
<html lang="en">
<head>
<meta charset="utf-8">
<title>Tampoli Fresh Market – Signage Design</title>
<link rel="stylesheet" href="https://fonts.googleapis.com/css2?family=Arimo&family=Open+Sans:wght@400;700;800&family=Russo+One&display=swap">
<style>
  :root {
    --paper: #ebe7de;
    --label-grey: #7d7d7d;
    --caption-grey: #6e6e6e;
    --market-red: #e8323a;
    --lime-light: #e4f6b0;
    --lime-mid: #b9e86a;
    --lime-deep: #8fd14a;
    --white: #ffffff;
  }
  * { margin: 0; padding: 0; box-sizing: border-box; }
  html, body { width: 1200px; height: 1000px; overflow: hidden; }
  body {
    position: relative;
    background: var(--paper);
    font-family: "Open Sans", sans-serif;
  }
  .board-title, .board-size {
    position: absolute;
    left: 43px;
    font-family: "Arimo", sans-serif;
    font-size: 40px;
    color: var(--label-grey);
  }
  .board-title { top: 55px; }
  .board-size { top: 150px; }
  .board-caption {
    position: absolute;
    left: 27px;
    top: 953px;
    font-size: 26px;
    color: var(--caption-grey);
  }

  .signboard {
    position: absolute;
    left: 9px;
    top: 391px;
    width: 1182px;
    height: 218px;
    overflow: hidden;
    background:
      radial-gradient(ellipse at 35% 30%, var(--lime-light) 0%, rgba(228,246,176,0) 55%),
      linear-gradient(100deg, var(--lime-mid) 0%, var(--lime-light) 45%, var(--lime-mid) 75%, var(--lime-deep) 100%);
  }
  .signboard-art { position: absolute; inset: 0; width: 100%; height: 100%; }

  .brand-mark {
    position: absolute;
    left: 496px;
    top: 20px;
    width: 190px;
    display: flex;
    align-items: center;
    justify-content: center;
    gap: 10px;
  }
  .brand-mark-square {
    width: 44px;
    height: 44px;
    background: var(--market-red);
  }
  .brand-mark-name {
    font-family: "Russo One", sans-serif;
    font-size: 34px;
    color: var(--market-red);
    line-height: 1;
  }
  .company-name {
    position: absolute;
    left: 496px;
    top: 100px;
    width: 190px;
    text-align: center;
    font-weight: 800;
    font-size: 14px;
    color: var(--market-red);
    white-space: nowrap;
  }
  .market-name {
    position: absolute;
    left: 318px;
    top: 138px;
    width: 570px;
    text-align: center;
    font-family: "Russo One", sans-serif;
    font-size: 40px;
    letter-spacing: 2px;
    color: var(--market-red);
    white-space: nowrap;
  }
  .address-tag {
    position: absolute;
    left: 789px;
    top: 0;
    width: 100px;
    height: 93px;
    background: var(--market-red);
    color: var(--white);
    text-align: center;
    font-weight: 700;
    padding-top: 20px;
    line-height: 1;
  }
  .address-unit { font-size: 32px; }
  .address-plaza { font-size: 10px; margin-top: 6px; }
  .address-lot { font-size: 12px; margin-top: 3px; }
</style>
</head>
<body>
  <h1 class="board-title">Final Design</h1>
  <p class="board-size">184 X 34 inch</p>

  <section class="signboard">
    <svg class="signboard-art" viewBox="0 0 1182 218" preserveAspectRatio="none">
      <defs>
        <linearGradient id="produce-tones" x1="0" y1="0" x2="1" y2="1">
          <stop offset="0" stop-color="#d9381f"/>
          <stop offset="0.45" stop-color="#b52a2f"/>
          <stop offset="0.75" stop-color="#7fae3a"/>
          <stop offset="1" stop-color="#4f8a2a"/>
        </linearGradient>
        <linearGradient id="poultry-tones" x1="0" y1="0" x2="1" y2="1">
          <stop offset="0" stop-color="#f2ded6"/>
          <stop offset="1" stop-color="#b8876a"/>
        </linearGradient>
        <linearGradient id="seafood-tones" x1="0" y1="0" x2="1" y2="1">
          <stop offset="0" stop-color="#9aa4ad"/>
          <stop offset="0.5" stop-color="#6f6f7a"/>
          <stop offset="1" stop-color="#a0614a"/>
        </linearGradient>
      </defs>
      <path role="img" aria-label="Photo of fresh vegetables: tomatoes, radishes, onions and lettuce"
            d="M0 0 H250 Q300 70 296 218 H0 Z" fill="url(#produce-tones)"/>
      <polygon points="880,0 1008,0 893,218 866,218" fill="#eefbc8" opacity="0.7"/>
      <polygon role="img" aria-label="Photo of raw chicken drumsticks on a board"
               points="1005,0 1182,0 1182,88 955,106" fill="url(#poultry-tones)"/>
      <polygon role="img" aria-label="Photo of fresh whole fish on a wooden board"
               points="955,106 1182,88 1182,218 890,218" fill="url(#seafood-tones)"/>
      <line x1="955" y1="106" x2="1182" y2="88" stroke="#ffffff" stroke-width="4"/>
    </svg>

    <div class="brand-mark">
      <span class="brand-mark-square"></span>
      <span class="brand-mark-name">BO KIAT</span>
    </div>
    <p class="company-name">BO KIAT MANAGEMENT</p>
    <h2 class="market-name">TAMPOLI FRESH MARKET</h2>

    <div class="address-tag">
      <div class="address-unit">204</div>
      <div class="address-plaza">KELVARA PLAZA</div>
      <div class="address-lot">#02-14</div>
    </div>
  </section>

  <p class="board-caption">Signage Design</p>
</body>
</html>
```